Open Red Harbor.. a non profit that seeks to stomp out skin cancer .. quiet paths toward opening red

Simple letterhead incorporating logo

Industry/Entity Type

Non Profit

Font styles to use
Sans Serif

Colors

Designer to choose colors to be used in the design.

```html
<!DOCTYPE html>
<html lang="en">
<head>
<meta charset="utf-8">
<title>Open Red Harbor Letterhead</title>
<link rel="stylesheet" href="https://fonts.googleapis.com/css2?family=Didact+Gothic&display=swap">
<style>
  :root {
    --backdrop: #544b4e;
    --paper: #f1f0ee;
    --navy: #2f3550;
    --sun: #f2e21a;
    --ink: #4a4e63;
    --rule: #8a8d9c;
  }
  html, body {
    margin: 0;
    padding: 0;
    width: 1200px;
    height: 925px;
    overflow: hidden;
    background: var(--backdrop);
    font-family: "Didact Gothic", "Century Gothic", sans-serif;
  }
  .letterhead {
    position: absolute;
    left: 300px;
    top: 37px;
    width: 600px;
    height: 850px;
    background: var(--paper);
    box-sizing: border-box;
  }
  .brand {
    position: absolute;
    top: 52px;
    right: 52px;
    display: flex;
    align-items: center;
    gap: 12px;
  }
  .brand-dot {
    width: 30px;
    height: 30px;
    border-radius: 50%;
    background: var(--navy);
  }
  .brand-name {
    font-size: 22px;
    color: var(--navy);
    letter-spacing: 0.5px;
  }
  .contact-footer {
    position: absolute;
    left: 60px;
    right: 60px;
    bottom: 50px;
    text-align: center;
    color: var(--ink);
    font-size: 10px;
    line-height: 1.6;
  }
  .contact-footer .rule {
    height: 0;
    border-top: 1px solid var(--rule);
  }
  .contact-footer .rule.top { margin-bottom: 8px; }
  .contact-footer .rule.bottom { margin-top: 8px; }
  .contact-footer b {
    font-weight: normal;
    color: var(--navy);
    text-decoration: underline;
    text-decoration-color: transparent;
  }
  .contact-footer .label { color: var(--navy); letter-spacing: 0.3px; }
  .contact-footer p { margin: 0; }
</style>
</head>
<body>
  <main class="letterhead">
    <header class="brand">
      <span class="brand-dot" aria-hidden="true"></span>
      <span class="brand-name">Open Red Harbor</span>
    </header>

    <footer class="contact-footer">
      <div class="rule top"></div>
      <p>Lindenweg 12, 50667 Köln · <span class="label">Tel:</span> +49 170 2284610 · <span class="label">Fax:</span> +49 170 2284611</p>
      <p><span class="label">Email:</span> hello@OpenRedHarbor.org · <span class="label">Web:</span> www.OpenRedHarbor.org</p>
      <div class="rule bottom"></div>
    </footer>
  </main>
</body>
</html>
```